" A consultoria será prestada de forma rápida e eficiente, ou seja, iremos prezar um alto relacionamento com os clientes juntamente com a entrega de um alto valor agregado (resultado). A empresa tem dois principais focos: resultado e satisfação do cliente. Tendo em nosso DNA a cultura do “One Stop Shop”, iremos ser altamente adaptáveis a mudanças, renovações, flexibilidade dos nossos clientes e do mercado em atuação e como um todo. Estaremos sempre atentos as novas tendências para que não fiquemos atrás da concorrência. As consultorias não serão muito longas, dado que visamos muito a eficiência e eficácia no atendimento. Além disso, as consultorias irão funcionar mais ou menos “sob demanda”, ou seja, iremos atender os clientes no horário que for acordado entre ambos, para que dessa forma, não fiquemos o dia inteiro no cliente, e somente o tempo necessário, otimizando assim o tempo do nosso cliente e sendo assim eficientes na resolução dos problemas encontrados. Resumidamente, será uma consultoria, dinâmica e express. Em termos de gestão, a empresa irá prezar pela cessante busca por conhecimento, constante investimento nos colaboradores da empresa, e em manter a empresa respirando GESTÃO. Incentivando sempre também o empreendedorismo e será um lugar aonde os colaboradores irão ter posturas de donos, para poderem ajudar no crescimento da empresa. Além disso, a consultoria irá fornecer outras duas soluções sendo elas o programa TAE (trilha ágil empreendedora) e Curso e treinamentos profissionalizantes. Esse irão funcionar da seguinte forma: O Programa TAE, Trilha Ágil Empreendedora, visamos auxiliar jovens empreendedores na construção de Novos Negócios e auxílio para o sucesso deles. Além disso, sendo auxiliados pela própria Consultoria. Cursos e treinamentos profissionalizantes (Coaching) para profissionais do mercado de trabalho, visando disseminar conhecimento e ajudá-los a se qualificarem. "

```html
<!DOCTYPE html>
<html lang="pt-BR">
<head>
<meta charset="utf-8">
<title>Velantra — Consultoria de Gestão</title>
<link href="https://fonts.googleapis.com/css2?family=Open+Sans:wght@400;600;700&display=swap" rel="stylesheet">
<style>
:root{
  --page-bg:#ffffff;
  --bar:#2d2f2e;
  --bar-dark:#1f2120;
  --green:#7cc443;
  --green-dark:#5fa630;
  --purple:#9d5bd8;
  --blue:#3e8ee3;
  --gray-box:#5d605f;
  --cream:#eeeddc;
  --ink:#3a3a3a;
  --muted:#8a8a80;
  --white:#ffffff;
  --red:#d9473c;
}
*{margin:0;padding:0;box-sizing:border-box}
html,body{width:1200px;height:1200px;overflow:hidden;background:var(--page-bg);font-family:"Open Sans",Arial,sans-serif;color:var(--ink)}
.page{position:absolute;left:312px;top:0;width:576px;height:1200px;overflow:hidden}
.abs{position:absolute}
.photo{position:absolute;left:0;width:576px}
.bar{position:absolute;left:0;width:576px;height:19px;background:var(--bar);display:flex;align-items:center;justify-content:space-between;padding:0 16px 0 96px}
.bar .mark{width:9px;height:9px;background:var(--green);border-radius:2px}
.nav{display:flex;gap:12px;font-size:6.5px;color:var(--white);font-weight:600}
.nav .on{color:var(--green)}
/* hero */
.hero{top:0;height:240px;background:linear-gradient(135deg,#6f8c86 0%,#9fb3ad 35%,#c7d2ce 55%,#7d9590 80%,#4e6661 100%)}
.hero-shade{position:absolute;inset:0;background:rgba(30,50,45,.28)}
.logo{position:absolute;left:92px;top:6px;display:flex;align-items:center;gap:5px;color:var(--white);font-weight:700;font-size:17px;letter-spacing:.3px}
.logo .dot{width:8px;height:8px;background:var(--green);border-radius:50%}
.hero .nav{position:absolute;right:60px;top:12px}
.hero-title{position:absolute;left:0;width:576px;top:92px;text-align:center;color:var(--white);font-size:11px;font-weight:600;line-height:1.35}
.btn{position:absolute;height:13px;border-radius:2px;color:var(--white);font-size:6px;font-weight:600;display:flex;align-items:center;justify-content:center}
.dots{position:absolute;right:50px;top:92px;display:flex;flex-direction:column;gap:8px}
.dots i{width:4px;height:4px;border-radius:50%;background:rgba(255,255,255,.6);display:block}
.dots i.on{background:var(--white)}
/* building */
.building{top:259px;height:144px;background:linear-gradient(100deg,#3f4a55 0%,#6b7680 30%,#a9b3bb 55%,#cfd6db 75%,#b9c2c9 100%)}
.sec-title{position:absolute;color:var(--white);font-size:10px;font-weight:600}
.sec-text{position:absolute;color:rgba(255,255,255,.85);font-size:5.5px;line-height:1.5}
/* boxes */
.boxes{position:absolute;top:403px;left:0;width:576px;height:77px;display:flex}
.box{flex:1;color:var(--white);text-align:center;padding-top:12px}
.box svg{display:block;margin:0 auto 6px}
.box h3{font-size:6.5px;font-weight:600}
.box p{font-size:5px;opacity:.85;margin-top:3px;padding:0 14px;line-height:1.4}
/* team */
.team{top:499px;height:221px;background:linear-gradient(180deg,#4b4e52 0%,#7e7b77 40%,#a59d93 65%,#6a6864 100%)}
.team-shade{position:absolute;inset:0;background:rgba(20,22,24,.25)}
.circle{position:absolute;width:30px;height:30px;border-radius:50%;background:var(--green);border:2px solid rgba(255,255,255,.7);display:flex;align-items:center;justify-content:center}
/* blog */
.blog{top:739px;height:221px;background:linear-gradient(180deg,#3e4140 0%,#7a7d7b 45%,#5a5d5b 75%,#3a3c3b 100%)}
.card{position:absolute;top:804px;width:113px;height:137px;background:var(--white)}
.card .pic{height:62px;background:linear-gradient(135deg,#b7a894,#e3ddd3 55%,#8d8273)}
.card .tag{position:absolute;left:6px;top:68px;background:var(--red);color:var(--white);font-size:4.5px;padding:1px 4px;font-weight:600}
.card h4{position:absolute;left:6px;top:78px;font-size:6px;font-weight:700;color:var(--ink)}
.card p{position:absolute;left:6px;right:6px;top:89px;font-size:4.8px;color:var(--muted);line-height:1.45}
/* contact */
.contact{position:absolute;top:979px;left:0;width:576px;height:192px;background:var(--cream)}
.contact h2{position:absolute;top:18px;width:576px;text-align:center;font-size:9px;font-weight:600;color:var(--ink);letter-spacing:.5px}
.contact .lead{position:absolute;top:31px;width:576px;text-align:center;font-size:5px;color:var(--muted)}
.field{position:absolute;left:108px;width:168px;height:12px;border-bottom:1px solid #c9c8b6;font-size:5px;color:var(--muted);padding-top:3px}
.send{position:absolute;left:108px;top:152px;width:50px;height:12px;background:#5b5c57;color:var(--white);font-size:5px;display:flex;align-items:center;justify-content:center}
.info{position:absolute;font-size:5px;color:var(--ink);line-height:1.55}
.info b{font-weight:700;display:block;font-size:5.5px}
.ic{position:absolute;width:6px;height:6px;border-radius:50%;background:var(--muted)}
.cols{position:absolute;font-size:4.8px;color:var(--muted);line-height:1.6}
.cols b{color:var(--ink);font-weight:700;display:block}
.footer{position:absolute;top:1171px;left:0;width:576px;height:29px;background:var(--bar-dark);display:flex;align-items:center;justify-content:space-between;padding:0 108px;font-size:5px;color:#9a9a9a}
.social{display:flex;gap:4px}
.social i{width:7px;height:7px;border-radius:50%;background:#cfcfcf;display:block}
</style>
</head>
<body>
<div class="page">

  <!-- Hero -->
  <section class="photo hero" role="img" aria-label="Mesa de trabalho vista de cima com gráficos, tablet e planta">
    <div class="hero-shade"></div>
    <div class="logo"><span class="dot"></span>Velantra</div>
    <nav class="nav"><span class="on">Home</span><span>Soluções</span><span>Cases</span><span>Sobre</span><span>Blog</span></nav>
    <h1 class="hero-title">Bem vindo à Velantra, sua consultoria<br>de gestão de negócios</h1>
    <div class="btn" style="left:240px;top:162px;width:96px;background:var(--green)">Saiba mais</div>
    <div class="dots"><i class="on"></i><i></i><i></i><i></i><i></i></div>
  </section>

  <div class="bar" style="top:240px"><span class="mark"></span><nav class="nav"><span class="on">Home</span><span>Soluções</span><span>Cases</span><span>Sobre</span><span>Blog</span></nav></div>

  <!-- Building -->
  <section class="photo building" role="img" aria-label="Fachada do prédio da consultoria com letreiro">
    <h2 class="sec-title" style="left:250px;top:33px">Lorem ipsum dolor sit amet</h2>
    <p class="sec-text" style="left:250px;top:50px;width:150px">Consultoria rápida e eficiente, com foco em resultado e satisfação do cliente.</p>
    <div class="btn" style="left:250px;top:110px;width:70px;background:var(--purple)">Saiba mais</div>
  </section>

  <div class="boxes">
    <div class="box" style="background:var(--green)">
      <svg width="14" height="14" viewBox="0 0 14 14"><circle cx="7" cy="7" r="6" fill="none" stroke="#fff" stroke-width="1.2"/><path d="M4 7l2 2 4-4" fill="none" stroke="#fff" stroke-width="1.2"/></svg>
      <h3>Consultoria express</h3><p>Atendimento sob demanda e eficiente</p>
    </div>
    <div class="box" style="background:var(--gray-box)">
      <svg width="14" height="14" viewBox="0 0 14 14"><rect x="2" y="3" width="10" height="8" fill="none" stroke="#fff" stroke-width="1.2"/><path d="M2 6h10" stroke="#fff" stroke-width="1.2"/></svg>
      <h3>Programa TAE</h3><p>Apoio a jovens empreendedores</p>
    </div>
    <div class="box" style="background:var(--blue)">
      <svg width="14" height="14" viewBox="0 0 14 14"><path d="M2 12V8M6 12V5M10 12V2" stroke="#fff" stroke-width="1.6"/></svg>
      <h3>Cursos e coaching</h3><p>Treinamentos para profissionais</p>
    </div>
    <div class="box" style="background:var(--purple)">
      <svg width="14" height="14" viewBox="0 0 14 14"><path d="M7 2l1.6 3.3 3.6.5-2.6 2.5.6 3.6L7 10.2 3.8 11.9l.6-3.6L1.8 5.8l3.6-.5z" fill="none" stroke="#fff" stroke-width="1.1"/></svg>
      <h3>Gestão de negócios</h3><p>Resultado com alto valor agregado</p>
    </div>
  </div>

  <div class="bar" style="top:480px"><span class="mark"></span><nav class="nav"><span class="on">Home</span><span>Soluções</span><span>Cases</span><span>Sobre</span><span>Blog</span></nav></div>

  <!-- Team -->
  <section class="photo team" role="img" aria-label="Equipe reunida unindo as mãos sobre a mesa">
    <div class="team-shade"></div>
    <h2 class="sec-title" style="left:216px;top:104px;font-size:7px">Metodologia TAE</h2>
    <p class="sec-text" style="left:216px;top:116px;width:100px">Trilha ágil para construir novos negócios com apoio da consultoria.</p>
    <div class="circle" style="left:129px;top:165px"><svg width="12" height="12" viewBox="0 0 12 12"><path d="M2 10V6M6 10V3M10 10V5" stroke="#fff" stroke-width="1.5"/></svg></div>
    <div class="circle" style="left:225px;top:165px"><svg width="12" height="12" viewBox="0 0 12 12"><circle cx="6" cy="6" r="4" fill="none" stroke="#fff" stroke-width="1.3"/></svg></div>
    <div class="circle" style="left:321px;top:165px"><svg width="12" height="12" viewBox="0 0 12 12"><path d="M2 6l3 3 5-6" fill="none" stroke="#fff" stroke-width="1.5"/></svg></div>
    <div class="dots" style="top:80px"><i></i><i class="on"></i><i></i></div>
  </section>

  <div class="bar" style="top:720px"><span class="mark"></span><nav class="nav"><span class="on">Home</span><span>Soluções</span><span>Cases</span><span>Sobre</span><span>Blog</span></nav></div>

  <!-- Blog -->
  <section class="photo blog" role="img" aria-label="Paisagem de montanhas em tons de cinza com pessoa no topo">
    <h2 class="sec-title" style="left:0;width:576px;text-align:center;top:22px">Lorem ipsum dolor sit amet</h2>
    <p class="sec-text" style="left:0;width:576px;text-align:center;top:37px">Novidades e tendências em gestão</p>
  </section>
  <article class="card" style="left:108px"><div class="pic" role="img" aria-label="Profissionais em reunião"></div><span class="tag">Gestão</span><h4>Gestão ágil</h4><p>Como otimizar o tempo do cliente com consultoria sob demanda.</p></article>
  <article class="card" style="left:230px"><div class="pic" role="img" aria-label="Equipe trabalhando em escritório"></div><span class="tag">Cursos</span><h4>Treinamentos</h4><p>Qualificação profissional para o mercado de trabalho atual.</p></article>
  <article class="card" style="left:352px"><div class="pic" role="img" aria-label="Pessoas conversando em grupo"></div><span class="tag">TAE</span><h4>Empreender</h4><p>Passos para tirar um novo negócio do papel com segurança.</p></article>

  <div class="bar" style="top:960px"><span class="mark"></span><nav class="nav"><span class="on">Home</span><span>Soluções</span><span>Cases</span><span>Sobre</span><span>Blog</span></nav></div>

  <!-- Contact -->
  <section class="contact">
    <h2>FALE CONOSCO</h2>
    <p class="lead">Envie sua mensagem e retornaremos em breve</p>
    <div class="field" style="top:58px">Nome</div>
    <div class="field" style="top:78px">E-mail</div>
    <div class="field" style="top:98px">Telefone</div>
    <div class="field" style="top:118px;height:26px">Mensagem</div>
    <div class="send">Enviar</div>
    <div class="info" style="left:290px;top:58px;width:90px"><b>Atendimento</b>Segunda a sexta<br>das 8h às 18h<br>Sob demanda</div>
    <span class="ic" style="left:392px;top:60px"></span><div class="info" style="left:402px;top:58px">Rua das Acácias, 210<br>São Paulo - SP</div>
    <span class="ic" style="left:392px;top:80px"></span><div class="info" style="left:402px;top:78px">(11) 4000-1234</div>
    <span class="ic" style="left:392px;top:93px"></span><div class="info" style="left:402px;top:91px">contato@velantra.com.br</div>
    <div class="cols" style="left:290px;top:132px"><b>Soluções</b>Consultoria<br>Programa TAE<br>Cursos</div>
    <div class="cols" style="left:352px;top:132px"><b>Empresa</b>Sobre nós<br>Cases<br>Blog</div>
    <div class="cols" style="left:414px;top:132px"><b>Ajuda</b>Contato<br>Suporte<br>Termos</div>
  </section>

  <footer class="footer"><span>© Velantra. Todos os direitos reservados.</span><div class="social"><i></i><i></i><i></i><i></i></div></footer>
</div>
</body>
</html>
```